Whole Body Cryotherapy Business needs a Brochure

We need a brochure for marketing events of our spa. The name of the business is FrostVale. Our website is www.glacierhaven.example. We are located in New York City at the Marlowe Arcade. We need an eye catching brochure that discusses the health benefits of whole body cryotherapy. We need an editable file to be able to tweak the language of the brochure. The contact information that should be on the brochure is as follows:

FrostVale
Marlowe Arcade, 482 W. 31st Avenue
New York, NY 10047

Phone: (855) 614-3098

EMail: glacierhaven@mailbox.example

We prefer a color scheme that mainly uses blue, but are open to any design that is eye catching.

We need the brochure to fit on 8.5" x 11" paper.

Requirements
Must have
• Must have space for the following paragraphs (use Lorem Ipsem and we can fill in later): (1) What is Whole Body Cryotherapy and (2) What makes FrostVale different.

```html
<!DOCTYPE html>
<html lang="en">
<head>
<meta charset="utf-8">
<title>FrostVale – Freeze Into Fitness</title>
<link rel="stylesheet" href="https://fonts.googleapis.com/css2?family=Montserrat:wght@400;500;600;700;800&display=swap">
<style>
  :root {
    --ice-blue: #1f6aa6;
    --ice-blue-deep: #14507f;
    --snow-blue: #3d7fb6;
    --white: #ffffff;
    --brand-indigo: #3e4cc2;
    --bullet-pink: #e2177f;
    --copy-violet: #4a3cc6;
  }
  * { margin: 0; padding: 0; box-sizing: border-box; }
  html, body { width: 927px; height: 1200px; overflow: hidden; background: var(--white); }
  body { font-family: "Montserrat", sans-serif; }
  .brochure { position: relative; width: 927px; height: 1200px; overflow: hidden; background: var(--white); }

  .hero-band {
    position: absolute; left: 0; top: 0; width: 927px; height: 380px;
    background: radial-gradient(ellipse at 40% 30%, #2f7fbd 0%, var(--ice-blue) 55%, var(--ice-blue-deep) 100%);
  }
  .snow-band {
    position: absolute; left: 0; top: 600px; width: 927px; height: 280px;
    background: linear-gradient(180deg, var(--snow-blue) 0%, #2a6ea7 100%);
  }
  .ribbon-swirl { position: absolute; left: 0; top: 0; width: 927px; height: 1200px; }

  .photo-model {
    position: absolute; left: 0; top: 180px; width: 340px; height: 1020px;
    background: linear-gradient(180deg, rgba(222,196,176,0.95) 0%, rgba(240,232,226,0.97) 45%, rgba(226,204,188,0.95) 100%);
    border-radius: 140px 140px 0 0;
  }

  .headline {
    position: absolute; left: 0; top: 38px; width: 927px; text-align: center;
    font-weight: 800; font-size: 72px; letter-spacing: 1px; color: var(--white); line-height: 1;
  }
  .section-title {
    position: absolute; text-align: right; text-transform: uppercase;
    font-weight: 500; letter-spacing: 1px; line-height: 1.16;
  }
  .section-title--what { top: 164px; right: 56px; font-size: 38.5px; color: var(--white); }
  .section-title--diff { top: 396px; right: 51px; font-size: 35px; color: var(--brand-indigo); }

  .intro-copy {
    position: absolute; left: 367px; top: 294px; width: 540px;
    font-size: 17.5px; line-height: 20px; color: var(--white);
  }
  .benefit-list { position: absolute; left: 384px; top: 487px; list-style: none; }
  .benefit-list li {
    display: flex; align-items: center; height: 30px;
    font-size: 15.5px; font-weight: 500; color: var(--copy-violet); white-space: nowrap;
  }
  .benefit-list svg { width: 18px; height: 18px; margin-right: 16px; flex: none; }

  .brand {
    position: absolute; left: 740px; top: 918px; width: 170px; text-align: center;
  }
  .brand-mark {
    display: block; width: 54px; height: 54px; margin: 0 auto 8px;
    border: 2px solid var(--brand-indigo); border-radius: 50%;
  }
  .brand-name { font-weight: 700; font-size: 25px; color: var(--brand-indigo); }

  .contact {
    position: absolute; right: 39px; top: 1041px; text-align: right; font-style: normal;
    color: var(--brand-indigo); font-weight: 500;
  }
  .contact p { font-size: 23px; line-height: 30px; white-space: nowrap; }
  .contact .contact-phone { font-size: 26px; line-height: 34px; }
  .contact .contact-email { font-size: 22px; margin-top: 10px; }
</style>
</head>
<body>
<main class="brochure">
  <div class="hero-band"></div>
  <div class="snow-band" role="img" aria-label="Winter backdrop of falling snowflakes"></div>

  <svg class="ribbon-swirl" viewBox="0 0 927 1200" role="img" aria-label="Decorative swirl of flowing pink, purple and blue ribbons">
    <defs>
      <linearGradient id="swirl-tones" x1="0.6" y1="0" x2="0.3" y2="1">
        <stop offset="0" stop-color="#e6338f"/>
        <stop offset="0.3" stop-color="#7a3fae"/>
        <stop offset="0.6" stop-color="#4f6fc9"/>
        <stop offset="0.85" stop-color="#5cc3ec"/>
        <stop offset="1" stop-color="#c6eef6"/>
      </linearGradient>
    </defs>
    <path d="M0 680 C 250 800, 520 880, 700 850 C 830 825, 905 710, 927 592 L927 930 C 820 1060, 640 1130, 420 1130 C 250 1125, 100 1100, 0 1080 Z" fill="url(#swirl-tones)"/>
  </svg>

  <div class="photo-model" role="img" aria-label="Photograph of a smiling woman in white sportswear stretching her arms overhead"></div>

  <h1 class="headline">FREEZE INTO FITNESS</h1>

  <h2 class="section-title section-title--what">What is whole body<br>cryotherapy ?</h2>
  <p class="intro-copy">Lorem ipsum dolor sit amet, consectetur adipiscing elit.<br>&nbsp;Fusce quis libero efficitur, vehicula velit ac, volutpat<br>augue. Proin cursus ex lectus, in feugiat est ultrices eu.</p>

  <h2 class="section-title section-title--diff">What makes FrostVale<br>different?</h2>
  <ul class="benefit-list">
    <li><svg viewBox="0 0 18 18"><path d="M3 2 L16 9 L3 16 Z" fill="none" stroke="var(--bullet-pink)" stroke-width="3" stroke-linejoin="round"/></svg>Lorem ipsum dolor sit amet, consectetur adipiscing elit.</li>
    <li><svg viewBox="0 0 18 18"><path d="M3 2 L16 9 L3 16 Z" fill="none" stroke="var(--bullet-pink)" stroke-width="3" stroke-linejoin="round"/></svg>Lorem ipsum dolor sit amet, consectetur adipiscing elit.</li>
    <li><svg viewBox="0 0 18 18"><path d="M3 2 L16 9 L3 16 Z" fill="none" stroke="var(--bullet-pink)" stroke-width="3" stroke-linejoin="round"/></svg>Lorem ipsum dolor sit amet, consectetur adipiscing elit.</li>
  </ul>

  <div class="brand">
    <span class="brand-mark"></span>
    <span class="brand-name">FrostVale</span>
  </div>

  <address class="contact">
    <p>Marlowe Arcade, 482 W. 31st Avenue</p>
    <p>New York, NY 10047</p>
    <p class="contact-phone">(855) 614-3098</p>
    <p class="contact-email">glacierhaven@mailbox.example</p>
  </address>
</main>
</body>
</html>
```